Banner Ad Design Project

We need a Banner to hang outside our Health Food Store to advertise to the public that we will be holding an Organic Market Day every Saturday.
We have our Business name and logo that will need to be incorporated into the design.
We want the design to convey freshness and have an earthy / farm feel, but also want the design to be crisp and not "Hippie"
we also need the banner to say "Fresh Organic Market every Saturday"
we will be selling fresh organic fruit and vegetables.
Target Market(s)
existing customers and general public walking past the shop
Industry/Entity Type
Farm
Look and feel

```html
<!DOCTYPE html>
<html lang="en">
<head>
<meta charset="utf-8">
<title>Fresh Organic Market – Every Saturday</title>
<link rel="stylesheet" href="https://fonts.googleapis.com/css2?family=Jost:wght@700&display=swap">
<style>
  :root {
    --straw: #e4c676;
    --rust: #b5462a;
  }
  html, body {
    margin: 0;
    padding: 0;
    width: 1200px;
    height: 800px;
    overflow: hidden;
    background: var(--straw);
  }
  .banner {
    display: block;
    width: 1200px;
    height: 800px;
  }
  .banner-bg { fill: var(--straw); }
  .banner-frame { fill: none; stroke: var(--rust); stroke-width: 10; }
  .headline {
    font-family: "Jost", sans-serif;
    font-weight: 700;
    text-transform: uppercase;
  }
  .headline--rust { fill: var(--rust); }
  .headline--straw { fill: var(--straw); }
  .market-box { fill: var(--rust); }
  .star-band { fill: var(--rust); }
  .store-name {
    font-family: "Jost", sans-serif;
    font-weight: 700;
    fill: var(--rust);
  }
</style>
</head>
<body>
<svg class="banner" viewBox="0 0 1200 800" xmlns="http://www.w3.org/2000/svg">
  <defs>
    <linearGradient id="hillside-fill" x1="0" y1="0" x2="1" y2="1">
      <stop offset="0" stop-color="#e4c676"/>
      <stop offset="0.55" stop-color="#c9774a"/>
      <stop offset="1" stop-color="#b5462a"/>
    </linearGradient>
  </defs>

  <rect class="banner-bg" x="0" y="0" width="1200" height="800"/>
  <rect class="banner-frame" x="12" y="12" width="1176" height="776"/>

  <text class="headline headline--rust" x="54" y="144" font-size="128"
        textLength="1092" lengthAdjust="spacingAndGlyphs">Fresh Organic</text>

  <rect class="market-box" x="54" y="180" width="1092" height="234"/>
  <text class="headline headline--straw" x="120" y="396" font-size="272"
        textLength="966" lengthAdjust="spacingAndGlyphs">Market</text>

  <text class="headline headline--rust" x="54" y="546" font-size="146"
        textLength="1092" lengthAdjust="spacingAndGlyphs">Every Saturday</text>

  <rect class="star-band" x="54" y="570" width="1092" height="24"
        role="img" aria-label="Decorative band with a row of small stars"/>

  <g class="store-mark">
    <text class="store-name" x="60" y="680" font-size="46">brookfield</text>
    <text class="store-name" x="60" y="744" font-size="46">wholefoods store</text>
  </g>

  <rect x="480" y="620" width="702" height="162" fill="url(#hillside-fill)"
        role="img" aria-label="Silhouette of a rolling farm hillside with trees"/>
</svg>
</body>
</html>
```